Simple Business Card Design

Professional/clean business card with custom logo included in layout.

Target Market(s)

N/A

Industry/Entity Type

Business

Contact Information for Business Card

Name: Marlene Hoskin, PT; NV Medicaid Provider; Phone: (775) 918-2467; Toll-free phone: (877) 406-1953; email: mar@copperfieldlaneventuresltd.example

Font styles to use
Serif
Decorative
Script

Requirements
Must have
• See "details" above.
Nice to have
• Would be interested to see dark vs. light/grayscale backgrounds that accentuate/contrast the logo colors. (I.e. dark navy background w/ white or grey text, etc.)

```html
<!DOCTYPE html>
<html lang="en">
<head>
<meta charset="utf-8">
<title>Marlene Hoskin, PT — Business Card</title>
<link rel="stylesheet" href="https://fonts.googleapis.com/css2?family=Cinzel:wght@400;600&family=Questrial&display=swap">
<style>
  :root {
    --backdrop: #2b2b2b;
    --navy: #121d3f;
    --navy-light: #1f2d5c;
    --band-grey: #8a8a8c;
    --band-grey-light: #b4b4b6;
    --cream: #f3ead0;
    --cream-light: #fbf8ee;
    --ink-navy: #1b2a5a;
    --accent-orange: #c9532b;
    --name-white: #ffffff;
  }
  html, body {
    margin: 0;
    width: 1200px;
    height: 863px;
    overflow: hidden;
    background: var(--backdrop);
  }
  .canvas {
    position: relative;
    width: 1200px;
    height: 863px;
  }
  .business-card {
    position: absolute;
    left: 180px;
    top: 191px;
    width: 840px;
    height: 480px;
    filter: drop-shadow(0 12px 24px rgba(0,0,0,0.45));
  }
  .card-name {
    font-family: "Cinzel", serif;
    font-weight: 600;
    font-size: 44px;
    letter-spacing: 1px;
    fill: var(--name-white);
  }
  .card-title {
    font-family: "Questrial", sans-serif;
    font-size: 20px;
    letter-spacing: 1.5px;
    fill: var(--accent-orange);
  }
  .card-contact {
    font-family: "Questrial", sans-serif;
    font-size: 20px;
    fill: var(--ink-navy);
  }
  .brand-name {
    font-family: "Cinzel", serif;
    font-weight: 400;
    font-size: 15px;
    letter-spacing: 1.5px;
    fill: var(--name-white);
  }
  .brand-dot { fill: var(--band-grey-light); }
</style>
</head>
<body>
<div class="canvas">
  <svg class="business-card" viewBox="0 0 840 480" width="840" height="480" aria-label="Business card for Marlene Hoskin, PT">
    <defs>
      <clipPath id="card-shape">
        <rect x="0" y="0" width="840" height="480" rx="24" ry="24"/>
      </clipPath>
      <linearGradient id="cream-fill" x1="0" y1="0" x2="0" y2="1">
        <stop offset="0" stop-color="var(--cream)"/>
        <stop offset="1" stop-color="var(--cream-light)"/>
      </linearGradient>
      <linearGradient id="grey-fill" x1="0" y1="0" x2="1" y2="1">
        <stop offset="0" stop-color="var(--band-grey)"/>
        <stop offset="1" stop-color="var(--band-grey-light)"/>
      </linearGradient>
      <radialGradient id="navy-fill" cx="0.6" cy="0.35" r="0.8">
        <stop offset="0" stop-color="var(--navy-light)"/>
        <stop offset="1" stop-color="var(--navy)"/>
      </radialGradient>
    </defs>

    <g clip-path="url(#card-shape)">
      <rect class="cream-band" x="0" y="0" width="840" height="480" fill="url(#cream-fill)"/>
      <path class="grey-arc" d="M0,0 H840 V480 H560 C450,360 250,290 0,290 Z" fill="url(#grey-fill)"/>
      <path class="navy-field" d="M0,0 H840 V480 H600 C500,330 260,220 0,170 Z" fill="url(#navy-fill)"/>
    </g>

    <g class="brand-mark">
      <circle class="brand-dot" cx="436" cy="110" r="9"/>
      <text class="brand-name" x="454" y="115">COPPERFIELD LANE</text>
    </g>

    <text class="card-name" x="120" y="218">MARLENE HOSKIN, PT</text>
    <text class="card-title" x="200" y="252">NV MEDICAID PROVIDER</text>

    <g class="card-contact" text-anchor="middle">
      <text x="290" y="330">Phone: (775) 918-2467</text>
      <text x="290" y="362">Toll-free phone: (877) 406-1953</text>
      <text x="270" y="394">Email: mar@copperfieldlaneventuresltd.example</text>
    </g>
  </svg>
</div>
</body>
</html>
```